Podcast cover art (not a logo)

I’m launching an audio-only podcast for parents of neurodivergent children. The podcast is meant to feel like a calm, trusted professional voice — not a brand or a performance.

Style direction:
--Clean and minimal
--Calm and grounded
--Professional, not playful
--Nothing flashy, loud, or busy
--No cartoon imagery

Content on the cover:
--Podcast title: Rooted in Listening
--Subtitle or tagline: Supporting Neurodivergent Kids with Science, Not Shame (or Understanding Neurodivergent Kids)
--No episode numbers, no dates

Design preferences:
--Text-forward design
--Neutral or soft colors (muted blues, grays, off-whites)
--High contrast for readability at small sizes
--Simple, timeless font

What I do NOT want:
--A logo or branding system
--Illustrations of children or families
--Bright colors or playful graphics
--Trendy fonts or visual effects

Technical requirements:
--Square image
--3000 × 3000 pixels
--RGB color mode
--JPEG or PNG
--File size under 500 KB

Deliverables:
--Final cover art file
--Optional: one or two alternate background color versions

```html
<!DOCTYPE html>
<html lang="en">
<head>
<meta charset="utf-8">
<title>Rooted in Listening — Podcast Cover</title>
<link rel="stylesheet" href="https://fonts.googleapis.com/css2?family=Playfair+Display:wght@500&family=Montserrat:wght@600&display=swap">
<style>
  :root {
    --page-bg: #ffffff;
    --frame: #efeee9;
    --cover-bg: #ffffff;
    --title-ink: #22384c;
    --tagline-ink: #23384b;
    --rule: #b9c3cc;
  }
  * { margin: 0; padding: 0; box-sizing: border-box; }
  html, body {
    width: 1200px;
    height: 807px;
    overflow: hidden;
    background: var(--page-bg);
  }
  .cover {
    position: absolute;
    left: 230px;
    top: 33px;
    width: 740px;
    height: 740px;
    background: var(--frame);
    padding: 26px;
  }
  .cover__inner {
    width: 100%;
    height: 100%;
    background: var(--cover-bg);
    display: flex;
    flex-direction: column;
    align-items: center;
    justify-content: center;
    padding: 40px;
    text-align: center;
  }
  .title {
    font-family: "Playfair Display", Georgia, serif;
    font-weight: 500;
    font-size: 100px;
    line-height: 1.12;
    letter-spacing: 0.01em;
    color: var(--title-ink);
  }
  .title__line {
    display: block;
  }
  .divider {
    width: 72px;
    height: 2px;
    background: var(--rule);
    margin: 44px 0 40px;
  }
  .tagline {
    font-family: "Montserrat", Arial, sans-serif;
    font-weight: 600;
    font-size: 19px;
    line-height: 1.6;
    letter-spacing: 0.2em;
    color: var(--tagline-ink);
    text-transform: uppercase;
  }
</style>
</head>
<body>
  <section class="cover" aria-label="Rooted in Listening podcast cover">
    <div class="cover__inner">
      <h1 class="title">
        <span class="title__line">Rooted in</span>
        <span class="title__line">Listening</span>
      </h1>
      <div class="divider" aria-hidden="true"></div>
      <p class="tagline">Understanding<br>Neurodivergent Kids</p>
    </div>
  </section>
</body>
</html>
```